Digital course framework design and style

We need a design for a framework to be used on an online course. The framework will have several layers and needs to have a style which can be followed throughout the course. The attached image is at the top level.

Need to keep to the triangle shape and the colour green and red for the words shown in the illustration. The three inner sections are pillars/pathways which we will expand out (Health, Adventure, Creativity) .
The course is Stuck to Striding (the inner section) so we need to show the flow from being frustrated with your kids on devices and not trying to be a successful and they can be, moving them to there kids taking action and frustration reducing. So important the framework has the feeling of progression and movement. The issue for each pillar/paths is the red text and the green being the result.

I want the framework to be simple to understand keeping to line diagram but introducing an icon for each piller/path. Needs to look professional and engaging.

I need to be able to edit the framework, present it elements so be in a format I can hide each Piller and display on a mouse click so layered.

Colours should fit into the brand colours

Core colour: #f07f37
Black secondary: #070707
Green : #0A633B
White: #FFFEFE

Website for brand approach: www.brightmovekids.example

Target Market(s)

Parents of children spending too long on devices

Font styles to use
Sans Serif

Requirements
Must have
• Clear and easy to see outcomes (green words on the example)
Flow from problem to solution (Stuck to Striding)
Style to be extended to further piller designs including icons for Health, Adventure, Creativity
Ability to present 1) the promise Stuck to Striding 2) each piller in turn
Brand colours included in brief
Should not have
• Busy complicated slide
Keep to line art not complex images

```html
<!DOCTYPE html>
<html lang="en">
<head>
<meta charset="utf-8">
<title>Stuck to Striding – Framework</title>
<link href="https://fonts.googleapis.com/css2?family=Montserrat:wght@300;400;700;800&display=swap" rel="stylesheet">
<style>
  :root {
    --green: #0A633B;
    --orange: #f07f37;
    --grey: #6d6e70;
    --white: #FFFEFE;
    --black: #070707;
    --shade-1: #1f7049;
    --shade-2: #347f5b;
    --shade-3: #4b8e6d;
    --shade-4: #619d80;
  }
  html, body {
    margin: 0;
    padding: 0;
    overflow: hidden;
    background: var(--white);
  }
  .framework {
    display: block;
    width: 1200px;
    height: 1000px;
    font-family: "Montserrat", sans-serif;
  }
  .outcome-disc { fill: var(--green); }
  .issue-band { fill: var(--grey); stroke: var(--white); stroke-width: 5; stroke-linejoin: round; }
  .pillar-band { fill: var(--orange); }
  .core { stroke: var(--white); stroke-width: 5; stroke-linejoin: round; }
  .core-0 { fill: var(--green); }
  .core-1 { fill: var(--shade-1); }
  .core-2 { fill: var(--shade-2); }
  .core-3 { fill: var(--shade-3); }
  .core-4 { fill: var(--shade-4); }
  .divider { stroke: var(--white); stroke-width: 5; stroke-linecap: round; }
  .outcome-text { fill: var(--white); font-weight: 800; font-size: 43px; text-anchor: middle; }
  .outcome-text--bottom { font-size: 40px; font-weight: 700; }
  .issue-text { fill: var(--white); font-weight: 300; font-size: 19.5px; text-anchor: middle; letter-spacing: 0.2px; }
  .promise-text { fill: var(--white); font-weight: 800; font-size: 35px; text-anchor: middle; }
  .promise-arrow { fill: var(--white); }
  .icon--on-band { color: var(--white); }
  .icon--legend { color: var(--orange); }
  .legend-label { fill: var(--orange); font-size: 16px; font-weight: 400; letter-spacing: 0.5px; }
  .brand-mark { fill: var(--orange); }
  .brand-name { fill: var(--orange); font-weight: 700; font-size: 24px; }
</style>
</head>
<body>
<svg class="framework" viewBox="0 0 1200 1000" xmlns="http://www.w3.org/2000/svg" role="img" aria-label="Stuck to Striding framework with Health, Creativity and Adventure pillars">
  <defs>
    <g id="icon-health" fill="none" stroke="currentColor">
      <path d="M0 8 C0 -4 16 -6 20 4 C24 -6 40 -4 40 8 C40 20 26 28 20 36 C14 28 0 20 0 8Z" fill="currentColor" stroke="none"/>
      <polyline points="-34,34 -24,34 -19,24 -13,44 -7,30 -2,34 4,34" stroke-width="2.5" stroke-linejoin="round" stroke-linecap="round"/>
    </g>
    <g id="icon-creativity" fill="none" stroke="currentColor" stroke-width="3" stroke-linejoin="round" stroke-linecap="round">
      <path d="M4 22 C-2 6 14 -4 28 0 C42 4 46 18 38 30 C32 38 20 42 12 38 C20 32 10 28 4 22Z"/>
      <circle cx="17" cy="12" r="3" fill="currentColor" stroke="none"/>
      <circle cx="30" cy="13" r="3" fill="currentColor" stroke="none"/>
      <circle cx="33" cy="26" r="3" fill="currentColor" stroke="none"/>
      <line x1="22" y1="22" x2="-8" y2="-6" stroke-width="4"/>
    </g>
    <g id="icon-adventure" fill="none" stroke="currentColor" stroke-width="2.5" stroke-linejoin="round">
      <polyline points="0,36 14,10 24,26 32,6 48,36"/>
      <polyline points="10,17 14,10 18,17" fill="currentColor"/>
      <polyline points="28,14 32,6 36,14" fill="currentColor"/>
      <g fill="currentColor" stroke="none">
        <circle cx="-4" cy="8" r="4"/>
        <circle cx="3" cy="5" r="5.5"/>
        <circle cx="10" cy="8" r="4"/>
        <rect x="-4" y="7" width="14" height="5" rx="2.5"/>
      </g>
    </g>
  </defs>

  <!-- Outcomes -->
  <circle class="outcome-disc" cx="598" cy="522" r="463"/>

  <!-- Issues band -->
  <polygon class="issue-band" points="598,59 197,753 999,753"/>

  <!-- Pillars band -->
  <polygon class="pillar-band" points="598,215 335,670 861,670"/>

  <!-- Core promise -->
  <g class="promise">
    <polygon class="core core-0" points="598,318 433.5,603 762.5,603"/>
    <g stroke="none">
      <polygon class="core-1" transform="translate(598 508) scale(0.8) translate(-598 -508)" points="598,318 433.5,603 762.5,603"/>
      <polygon class="core-2" transform="translate(598 508) scale(0.6) translate(-598 -508)" points="598,318 433.5,603 762.5,603"/>
      <polygon class="core-3" transform="translate(598 508) scale(0.4) translate(-598 -508)" points="598,318 433.5,603 762.5,603"/>
      <polygon class="core-4" transform="translate(598 508) scale(0.2) translate(-598 -508)" points="598,318 433.5,603 762.5,603"/>
    </g>
    <text class="promise-text" x="598" y="482">STRIDING</text>
    <polygon class="promise-arrow" points="598,508 587,528 609,528"/>
    <text class="promise-text" x="598" y="592">STUCK</text>
  </g>

  <!-- Dividers -->
  <line class="divider" x1="598" y1="59" x2="598" y2="318"/>
  <line class="divider" x1="197" y1="753" x2="433.5" y2="603"/>
  <line class="divider" x1="999" y1="753" x2="762.5" y2="603"/>

  <!-- Health pillar -->
  <g class="pillar pillar--health">
    <text class="outcome-text" transform="translate(318 355) rotate(-60)">
      <tspan x="0" y="-6">Balanced, Fit,</tspan>
      <tspan x="0" y="48">Energetic &amp; Focused</tspan>
    </text>
    <text class="issue-text" transform="translate(432 405) rotate(-60)">Anxious, Overweight, Unfit &amp; Disconnected</text>
    <use class="icon--on-band" href="#icon-health" transform="translate(486 415) scale(0.95)"/>
  </g>

  <!-- Creativity pillar -->
  <g class="pillar pillar--creativity">
    <text class="outcome-text" transform="translate(878 355) rotate(60)">
      <tspan x="0" y="-6">Bright, Idea Driven,</tspan>
      <tspan x="0" y="48">Positive &amp; Motivated</tspan>
    </text>
    <text class="issue-text" transform="translate(764 405) rotate(60)">Unimaginative, negative, screen focused &amp; trapped</text>
    <use class="icon--on-band" href="#icon-creativity" transform="translate(690 428) scale(0.95)"/>
  </g>

  <!-- Adventure pillar -->
  <g class="pillar pillar--adventure">
    <text class="outcome-text outcome-text--bottom" x="598" y="813">Curious, Connected,</text>
    <text class="outcome-text outcome-text--bottom" x="598" y="862">Excited &amp; Leading</text>
    <text class="issue-text" x="598" y="718">Inactive, Insular, Solitary &amp; Timid</text>
    <use class="icon--on-band" href="#icon-adventure" transform="translate(578 620) scale(0.9)"/>
  </g>

  <!-- Legend -->
  <g class="legend">
    <use class="icon--legend" href="#icon-health" transform="translate(72 866) scale(0.5)"/>
    <text class="legend-label" x="106" y="882">HEALTH</text>
    <use class="icon--legend" href="#icon-creativity" transform="translate(68 908) scale(0.5)"/>
    <text class="legend-label" x="106" y="922">CREATIVITY</text>
    <use class="icon--legend" href="#icon-adventure" transform="translate(66 946) scale(0.5)"/>
    <text class="legend-label" x="106" y="962">ADVENTURE</text>
  </g>

  <!-- Brand -->
  <g class="brand">
    <rect class="brand-mark" x="944" y="937" width="18" height="18"/>
    <text class="brand-name" x="972" y="954">BrightMove Kids</text>
  </g>
</svg>
</body>
</html>
```